HARLOWE FREIGHT & PLANT HIRE NEEDS A FLYER

WE NEED A FLYER FOR OUR COMPANY <br/>WE SPECIALISE IN ROAD BUILDING AND MAINTENANCE, GENERAL EARTHWORK DAM REPAIRS & DESILTING, FENCE CLEARING, FIRE BREAKS, GRAVEL SOURCE AND DELIVERY GENERAL FREIGHT STEEL HAY LICK AND MCHINERY. <br/><br/>I HAVE UPLOAD A FILE THAT I LIKE AND WOULD LIKE SOMETHING THE SAME IF POSSIBLE. AND LOGO TO GO WITH IT.

```html
<!DOCTYPE html>
<html lang="en">
<head>
<meta charset="utf-8">
<title>Harlowe Freight &amp; Plant Hire Flyer</title>
<link href="https://fonts.googleapis.com/css2?family=Russo+One&family=Lato:wght@400;700&display=swap" rel="stylesheet">
<style>
  :root{
    --stage:#616062;
    --paper:#ffffff;
    --charcoal:#3b3b3d;
    --charcoal-deep:#333335;
    --amber:#f5a91c;
    --ink:#1c1c1c;
    --light:#f2f2f2;
  }
  html,body{margin:0;padding:0;overflow:hidden}
  body{width:1200px;height:1200px;background:var(--stage);position:relative}
  .flyer{
    position:absolute;left:270px;top:100px;width:889px;height:1247px;
    transform:scale(0.8);transform-origin:0 0;
    background:var(--paper);box-shadow:0 12px 30px rgba(0,0,0,.45);overflow:hidden;
    font-family:"Lato",sans-serif;
  }
  .flyer-bg{position:absolute;inset:0}
  .brand{position:absolute;left:32px;top:60px;font-family:"Russo One",sans-serif;color:var(--charcoal);line-height:1.05}
  .brand-name{font-size:52px;letter-spacing:1px}
  .brand-sub{font-size:28px}
  .contact{position:absolute;right:44px;top:32px;text-align:right}
  .contact-names{font-family:"Russo One",sans-serif;font-size:29px;color:var(--ink);letter-spacing:.5px}
  .contact-phone{font-family:"Russo One",sans-serif;font-size:36px;color:var(--amber);display:flex;align-items:center;justify-content:flex-end;gap:4px;line-height:1}
  .contact-email{font-size:16px;color:var(--ink);display:flex;align-items:center;justify-content:flex-end;gap:10px;margin-top:6px;padding-right:78px}
  .section-title{position:absolute;font-family:"Russo One",sans-serif;color:var(--amber);font-size:24px;line-height:1.1;margin:0;font-weight:400}
  .title-specialising{left:102px;top:805px}
  .title-machinery{left:511px;top:780px}
  .checklist{position:absolute;list-style:none;margin:0;padding:0;color:var(--light);font-size:17px;line-height:21px}
  .checklist li{position:relative;padding-left:24px}
  .checklist li::before{
    content:"";position:absolute;left:0;top:4px;width:6px;height:11px;
    border-right:2px solid var(--amber);border-bottom:2px solid var(--amber);transform:rotate(40deg);
  }
  .list-specialising{left:89px;top:858px;width:300px}
  .list-specialising li{margin-bottom:14px}
  .list-machinery{left:528px;top:846px}
  .list-machinery li{margin-bottom:12.5px}
  .divider{position:absolute;left:419px;top:818px;width:3px;height:382px;background:var(--amber);border-radius:2px}
  .footer-bar{position:absolute;left:0;bottom:0;width:100%;height:12px;background:var(--amber)}
</style>
</head>
<body>
<div class="flyer">
  <svg class="flyer-bg" width="889" height="1247" viewBox="0 0 889 1247">
    <defs>
      <linearGradient id="photoTone" x1="0" y1="0" x2="1" y2="1">
        <stop offset="0" stop-color="#e8b08a"/>
        <stop offset="0.45" stop-color="#c9504a"/>
        <stop offset="1" stop-color="#2c3a55"/>
      </linearGradient>
      <linearGradient id="rollerTone" x1="0" y1="0" x2="0" y2="1">
        <stop offset="0" stop-color="#3f8fd8"/>
        <stop offset="0.6" stop-color="#c0572a"/>
        <stop offset="1" stop-color="#2a2d33"/>
      </linearGradient>
    </defs>
    <path d="M0 560 Q300 760 889 560 L889 1247 L0 1247 Z" fill="var(--charcoal)"/>
    <path d="M0 358 Q470 40 889 265 L889 310 Q470 120 0 380 Z" fill="var(--amber)"/>
    <path d="M0 350 Q470 30 889 258 L889 268 Q470 44 0 362 Z" fill="var(--charcoal)"/>
    <path d="M0 600 Q200 770 889 560 L889 590 Q220 800 0 640 Z" fill="var(--amber)"/>
    <path d="M0 380 Q470 120 889 310 L889 560 Q200 770 0 600 Z" fill="url(#photoTone)" role="img" aria-label="Photo of a red prime mover with a white trailer in front of a container port"/>
    <circle cx="127" cy="655" r="116" fill="var(--amber)"/>
    <circle cx="127" cy="655" r="107" fill="var(--paper)"/>
    <circle cx="127" cy="655" r="99" fill="url(#rollerTone)" role="img" aria-label="Photo of a road roller working on fresh asphalt"/>
  </svg>

  <div class="brand">
    <div class="brand-name">HARLOWE</div>
    <div class="brand-sub">FREIGHT &amp; PLANT HIRE</div>
  </div>

  <div class="contact">
    <div class="contact-names">DEAN &amp; MARLEE</div>
    <div class="contact-phone">
      <svg width="26" height="26" viewBox="0 0 24 24" aria-hidden="true"><circle cx="12" cy="12" r="10.5" fill="none" stroke="#1c1c1c" stroke-width="1.6"/><path d="M8.5 7c1-.6 1.6 1.4 1.9 2 .3.7-.9 1-.6 1.7.6 1.3 1.5 2.2 2.8 2.8.7.3 1-.9 1.7-.6.6.3 2.6.9 2 1.9-.5 1-1.7 1.8-3 1.2-2.8-1.3-4.8-3.3-6-6-.6-1.3.2-2.5 1.2-3z" fill="#1c1c1c"/></svg>
      0491570168
    </div>
    <div class="contact-email">
      <svg width="16" height="12" viewBox="0 0 16 12" aria-hidden="true"><rect x="0" y="0" width="16" height="12" fill="#1c1c1c"/><path d="M0 0 L8 7 L16 0" fill="none" stroke="#fff" stroke-width="1.3"/></svg>
      marlee.voss@mailbox.com
    </div>
  </div>

  <h2 class="section-title title-specialising">SPECIALISING IN</h2>
  <ul class="checklist list-specialising">
    <li>Road Building&amp; Maintenance</li>
    <li>General Earthwork Dam Repairs &amp; Desilting</li>
    <li>Fence Clearing</li>
    <li>Fire Breaks</li>
    <li>Gravel Source &amp;<br>Delivery General</li>
    <li>Freight Steel</li>
    <li>Hay</li>
    <li>Lick</li>
    <li>Machinery</li>
  </ul>

  <div class="divider"></div>

  <h2 class="section-title title-machinery">CURRENT MACHINERY<br>AVAILABLE</h2>
  <ul class="checklist list-machinery">
    <li>Grader</li>
    <li>Loader &amp; Stick Rack</li>
    <li>Rollers</li>
    <li>Dozer</li>
    <li>Water Trucks</li>
    <li>Side Tippers</li>
    <li>Prime Movers</li>
    <li>Forklift</li>
    <li>Skid Steer Loader</li>
    <li>Flat tops</li>
    <li>Drop Deck</li>
  </ul>

  <div class="footer-bar"></div>
</div>
</body>
</html>
```